Bright Mesh Business Card

This is a business card for a printing company but I actually don't have a logo. Just need to typeset the words "Bright Mesh Printing" as the logo. Then add my name "Loretta Vance" + phone number + address

Target Market(s)

ceos and professionals

Industry/Entity Type

printing and manufacturing

Contact Information for Business Card

Bright Mesh Printing/ 4617 calloway st. S. Marlow Springs, NV 91648/ 555-417-3980/ Loretta Vance

Font styles to use
Serif
Other font styles liked:
• a modern font would be nice

Colors
0054AA
0677BA
7BADD7
CADEEF
E8F1F8
0094D4
00A9DD
6FCCEA
C7EBF8
E9F6FB

Requirements
Must have
• company name, number, address
Nice to have
• nice bold feel
Should not have
• nothing in particular

```html
<!DOCTYPE html>
<html lang="en">
<head>
<meta charset="utf-8">
<title>Bright Mesh Printing – Business Card</title>
<link rel="stylesheet" href="https://fonts.googleapis.com/css2?family=Roboto:wght@400;700&family=Roboto+Condensed:wght@700&display=swap">
<style>
  :root {
    --backdrop: #2c2c2c;
    --brand-blue: #0670b6;
    --brand-blue-deep: #0563a8;
    --accent-light: #7badd7;
    --card-white: #f3f3f3;
    --card-white-shade: #e4e4e4;
    --divider-dark: #3b4048;
    --ink: #333740;
    --name-blue: #0670b6;
    --text-white: #f2f4f7;
  }
  * { box-sizing: border-box; margin: 0; padding: 0; }
  html, body {
    width: 1200px; height: 1138px; overflow: hidden;
    background: var(--backdrop);
    font-family: "Roboto", Arial, sans-serif;
  }
  .card {
    position: absolute; left: 274px; width: 624px; height: 376px;
    border-radius: 16px; overflow: hidden;
  }
  .card--front {
    top: 185px;
    background: linear-gradient(180deg, var(--brand-blue) 0%, var(--brand-blue-deep) 100%);
  }
  .card--back {
    top: 607px;
    background: linear-gradient(160deg, var(--card-white) 0%, var(--card-white-shade) 100%);
  }
  .wordmark {
    position: absolute; text-align: center; color: var(--text-white);
    font-family: "Roboto", Arial, sans-serif; font-weight: 700;
  }
  .wordmark__dot {
    display: block; margin: 0 auto; border-radius: 50%;
    background: var(--accent-light);
  }
  .wordmark__name { display: block; line-height: 1; letter-spacing: 0.01em; }
  .wordmark__sub { display: block; line-height: 1; letter-spacing: 0.62em; margin-right: -0.62em; }

  .card--front .wordmark { left: 0; right: 0; top: 90px; }
  .card--front .wordmark__dot { width: 84px; height: 84px; margin-bottom: 36px; }
  .card--front .wordmark__name { font-size: 44px; }
  .card--front .wordmark__sub { font-size: 20px; margin-top: 12px; }

  .back-panel { position: absolute; left: 0; top: 0; width: 624px; height: 376px; }
  .card--back .wordmark { left: 20px; width: 284px; top: 100px; }
  .card--back .wordmark__dot { width: 78px; height: 78px; margin-bottom: 30px; }
  .card--back .wordmark__name { font-size: 36px; }
  .card--back .wordmark__sub { font-size: 17px; margin-top: 11px; }

  .contact { position: absolute; left: 378px; top: 115px; color: var(--ink); }
  .contact__name {
    font-family: "Roboto Condensed", "Arial Narrow", sans-serif; font-weight: 700;
    font-size: 25px; color: var(--name-blue); line-height: 1;
  }
  .contact__title { font-size: 16px; margin-top: 7px; }
  .contact__list { list-style: none; margin-top: 22px; font-size: 16.5px; line-height: 24px; }
  .contact__item { position: relative; padding-left: 29px; }
  .contact__icon { position: absolute; left: 0; top: 4px; width: 16px; height: 16px; }
</style>
</head>
<body>
  <section class="card card--front" aria-label="Card front">
    <div class="wordmark">
      <span class="wordmark__dot"></span>
      <span class="wordmark__name">BRIGHT MESH</span>
      <span class="wordmark__sub">PRINTING</span>
    </div>
  </section>

  <section class="card card--back" aria-label="Card back">
    <svg class="back-panel" viewBox="0 0 624 376" aria-hidden="true">
      <path d="M0 0 H284 Q406 188 280 376 H0 Z" fill="var(--divider-dark)"/>
      <path d="M0 0 H276 Q396 188 272 376 H0 Z" fill="var(--brand-blue)"/>
    </svg>
    <div class="wordmark">
      <span class="wordmark__dot"></span>
      <span class="wordmark__name">BRIGHT MESH</span>
      <span class="wordmark__sub">PRINTING</span>
    </div>
    <div class="contact">
      <p class="contact__name">Loretta Vance</p>
      <p class="contact__title">Managing Director</p>
      <ul class="contact__list">
        <li class="contact__item">
          <svg class="contact__icon" viewBox="0 0 16 16" aria-hidden="true">
            <circle cx="8" cy="8" r="7" fill="none" stroke="var(--name-blue)" stroke-width="1.6"/>
            <path d="M5.6 4.6l1.2 1.6-.7.9c.5 1 1.3 1.8 2.3 2.3l.9-.7 1.6 1.2-.6 1.2c-2.6-.3-4.7-2.4-5-5z" fill="var(--name-blue)"/>
          </svg>
          555-417-3980
        </li>
        <li class="contact__item">
          <svg class="contact__icon" viewBox="0 0 16 16" aria-hidden="true">
            <path d="M8 0.5a5.6 5.6 0 0 0-5.6 5.6C2.4 10.3 8 15.8 8 15.8s5.6-5.5 5.6-9.7A5.6 5.6 0 0 0 8 .5zm0 8a2.4 2.4 0 1 1 0-4.8 2.4 2.4 0 0 1 0 4.8z" fill="var(--name-blue)"/>
          </svg>
          4617 Calloway St. S.<br>Marlow Springs, NV 91648
        </li>
      </ul>
    </div>
  </section>
</body>
</html>
```